Tide of the Modest : Thriving amid network change by Curtis Oyelaran

Need a book cover, front, back and 3D. We would like the cover to have a digital globe that also shows blockchain/nodes. Best if it can also illustrate the idea of Tide of the modest. Please see the pictures which I have short-listed which can be potentially used for the book cover.

The book cover should look like an expert book and I have attached some graphics that we can potentially buy and use for this book cover.

The text for the back cover is attached in the docx. Some text is not finished, please leave empty spaces for this.

Target Market(s)

Those interested in technology, blockchain, business, finance and law. The more informed readers.

Industry/Entity Type

Digital

Font styles to use
Sans Serif

Colors
31a5d6
0555a3
33a6d7
3176b5
85cae6
85acd3
cee9f5
cedeed

Requirements
Must have
• We would like you to consider the images attached here for the book design. We want it to be simple, clear and like an expert book. Please refer to the docx for the back cover text. Leave some text spaces for text not yet written.
• We require, front cover, back cover and 3D. You can do the 3D after your design is selected.
Nice to have
• The cover should be classy and timeless. It should have the blockchain / nodes. Will be great if the book cover can convey the meaning of Tide of the Modest, through the text. eg. one of the images, look like a "Lanternfall" type photo, maybe the text can be somewhat Lanternfall like.
• You are welcome to suggest photos not attached here.
• Once we have identified the winner, we will proceed to purchase the photo for our use.
• Text can be Lato, but not necessary.
Should not have
• Too messy or too many ideas. Just a simple clear idea.

```html
<!DOCTYPE html>
<html lang="en">
<head>
<meta charset="utf-8">
<title>Tide of the Modest — Front Cover</title>
<link rel="stylesheet" href="https://fonts.googleapis.com/css2?family=Montserrat:wght@400;600;800;900&display=swap">
<style>
  :root {
    --page-bg: #ffffff;
    --cover-black: #05070c;
    --cover-navy: #0a1424;
    --ink-white: #ffffff;
    --gold-light: #fbe27a;
    --gold-mid: #e0a91c;
    --gold-deep: #b8790a;
    --globe-bright: #85cae6;
    --globe-mid: #31a5d6;
    --globe-deep: #0555a3;
    --globe-dark: #0b2a4f;
  }
  * { box-sizing: border-box; margin: 0; padding: 0; }
  html, body {
    width: 1200px;
    height: 1200px;
    overflow: hidden;
    background: var(--page-bg);
  }
  .canvas {
    width: 1200px;
    height: 1200px;
    display: flex;
    align-items: center;
    justify-content: center;
  }
  .book-cover {
    position: relative;
    width: 734px;
    height: 1100px;
    background: linear-gradient(180deg, var(--cover-black) 0%, var(--cover-navy) 55%, var(--cover-black) 100%);
    overflow: hidden;
    font-family: "Montserrat", sans-serif;
    color: var(--ink-white);
  }
  .cover-tagline {
    position: absolute;
    top: 78px;
    left: 0;
    right: 0;
    text-align: center;
    font-size: 15px;
    font-weight: 600;
    letter-spacing: 0.42em;
    text-transform: uppercase;
  }
  .cover-title {
    position: absolute;
    top: 160px;
    left: 0;
    right: 0;
    text-align: center;
  }
  .title-main {
    display: inline-block;
    font-size: 170px;
    font-weight: 900;
    line-height: 1;
    letter-spacing: -0.01em;
    background: linear-gradient(170deg, var(--gold-light) 0%, var(--gold-mid) 45%, var(--gold-deep) 70%, var(--gold-light) 100%);
    -webkit-background-clip: text;
    background-clip: text;
    color: transparent;
  }
  .title-sub {
    display: block;
    margin-top: 2px;
    padding-left: 150px;
    font-size: 22px;
    font-weight: 800;
    letter-spacing: 0.12em;
    text-transform: uppercase;
  }
  .cover-globe {
    position: absolute;
    left: -120px;
    right: -120px;
    top: 470px;
    height: 620px;
    background:
      radial-gradient(ellipse 60% 18% at 50% 10%, rgba(206,233,245,0.55) 0%, rgba(133,202,230,0.25) 40%, transparent 75%),
      radial-gradient(ellipse 55% 70% at 50% 70%, var(--globe-mid) 0%, var(--globe-deep) 45%, var(--globe-dark) 75%, transparent 100%);
  }
  .cover-author {
    position: absolute;
    bottom: 150px;
    left: 0;
    right: 0;
    text-align: center;
    line-height: 1.2;
  }
  .author-by {
    display: block;
    font-size: 22px;
    font-weight: 800;
  }
  .author-name {
    display: block;
    font-size: 34px;
    font-weight: 800;
  }
</style>
</head>
<body>
<main class="canvas">
  <article class="book-cover">
    <div class="cover-globe" role="img" aria-label="Glowing blue digital globe wrapped in a network of light trails and blockchain nodes"></div>
    <p class="cover-tagline">Thriving amid network change</p>
    <h1 class="cover-title">
      <span class="title-main">TIDE</span>
      <span class="title-sub">of the modest</span>
    </h1>
    <p class="cover-author">
      <span class="author-by">By</span>
      <span class="author-name">Curtis Oyelaran</span>
    </p>
  </article>
</main>
</body>
</html>
```